Marwick Ostrand Law website for a law firm

modern clean website for a small boutique law firm. Based in Sacramento, CA and the Bay Area. Practice areas of Family Law, Civil litigation, and Criminal Defense. We already have a logo design as well as attorney pictures to include on page.
Would like images of California included on site.
Would like site to go with Logo that is already designed...blue/grey/white colors.

Industry/Entity Type

Law Firm

Number of Pages Required

5+ page

Requirements
Must have
• I already have several pages of content drafted. Just need the pages with images to input content. Must be clean and modern feel. Want it to reflect California and small boutique feel that is provided personalized legal attention.
• Must have a page where I can blog or post articles on.

```html
<!DOCTYPE html>
<html lang="en">
<head>
<meta charset="UTF-8">
<title>Marwick Ostrand Law</title>
<link href="https://fonts.googleapis.com/css2?family=Jost:wght@300;400;500;600&display=swap" rel="stylesheet">
<style>
:root{
  --blue:#3f86c8;
  --blue-light:#6fb0e4;
  --blue-band:#4a8fd0;
  --box:#6ea6da;
  --ink:#3a3a3a;
  --muted:#777;
  --dark:#333335;
  --darker:#242426;
  --grey-bg:#eeeeee;
  --white:#ffffff;
}
*{box-sizing:border-box;margin:0;padding:0}
html,body{width:1200px;height:2904px;overflow:hidden}
body{font-family:"Jost",sans-serif;color:var(--ink);background:var(--white);position:relative}
.section-title{font-size:44px;font-weight:500;text-align:center;letter-spacing:1px;text-transform:uppercase}
.btn{display:inline-block;background:var(--blue);color:var(--white);font-size:17px;font-weight:500;padding:14px 26px;letter-spacing:1px;text-transform:uppercase}

/* nav */
.site-nav{position:absolute;top:0;left:0;width:1200px;height:72px;background:var(--white);display:flex;align-items:center;justify-content:space-between;padding:0 60px;z-index:2}
.brand{font-size:40px;font-weight:500;color:var(--ink);letter-spacing:1px}
.menu{display:flex;gap:6px;list-style:none}
.menu li{font-size:15px;font-weight:500;padding:12px 20px;color:var(--ink);letter-spacing:1px}
.menu li.active{background:var(--blue);color:var(--white)}

/* hero */
.hero{position:absolute;top:0;left:0;width:1200px;height:680px;background:linear-gradient(180deg,#c9d9e6 0%,#9fc0dc 35%,#3b6fa4 62%,#214a78 80%,#4f86b8 100%)}
.hero-text{position:absolute;top:390px;width:100%;text-align:center}
.hero-text h1{color:var(--white);font-size:66px;font-weight:500;letter-spacing:2px}
.hero-text p{color:var(--blue-light);font-size:44px;font-weight:400;line-height:1.1;margin-top:6px;letter-spacing:1px}

/* welcome */
.welcome{position:absolute;top:680px;left:0;width:1200px;height:340px;text-align:center;padding-top:54px}
.welcome .section-title span{color:var(--blue)}
.welcome p{width:880px;margin:22px auto 30px;font-size:16px;line-height:1.45;color:var(--muted)}

/* practice */
.practice{position:absolute;top:1020px;left:0;width:1200px;height:428px;background:var(--blue-band);padding-top:50px}
.practice .section-title{color:var(--white)}
.practice-grid{display:flex;gap:40px;justify-content:center;margin-top:36px}
.practice-card{width:320px;height:250px;background:var(--box);display:flex;flex-direction:column;align-items:center;padding-top:32px}
.practice-card svg{width:130px;height:130px}
.practice-card h3{color:var(--white);font-size:30px;font-weight:500;margin-top:22px;text-transform:uppercase}

/* contact */
.contact{position:absolute;top:1448px;left:0;width:1200px;height:252px;background:var(--dark);padding-top:38px;text-align:center}
.contact .section-title{color:var(--white)}
.contact-form{display:flex;justify-content:center;gap:12px;margin-top:24px}
.field{width:200px;height:44px;background:var(--white);text-align:left;padding:12px 16px;font-size:15px;color:#888}
.field.wide{width:260px}
.contact-form .btn{padding:12px 26px}

/* team */
.team{position:absolute;top:1700px;left:0;width:1200px;height:300px;padding-top:34px}
.team-grid{display:flex;gap:80px;padding:0 72px;margin-top:26px}
.member{display:flex;gap:24px;width:500px}
.member .photo{width:130px;height:130px;flex:none;background:linear-gradient(135deg,#8aa0b4,#4d6176)}
.member h4{color:var(--blue);font-size:22px;font-weight:500}
.member p{font-size:14px;color:var(--muted);line-height:1.4;margin:6px 0 8px}
.more{font-size:13px;font-weight:600;text-transform:uppercase;color:var(--ink)}

/* blog */
.blog{position:absolute;top:2000px;left:0;width:1200px;height:560px;background:var(--grey-bg);padding-top:36px}
.blog-grid{display:flex;gap:40px;justify-content:center;margin-top:30px}
.post{width:320px}
.post .thumb{height:200px;position:relative}
.post .date{position:absolute;left:0;bottom:-20px;width:60px;height:64px;background:var(--blue);color:var(--white);text-align:center;padding-top:6px;line-height:1}
.post .date b{display:block;font-size:28px;font-weight:500}
.post .date span{font-size:15px}
.post h5{font-size:17px;font-weight:500;line-height:1.25;margin:10px 0 8px 72px;color:var(--ink)}
.post p{font-size:14px;color:var(--muted);line-height:1.4;margin:14px 0 8px}

/* footer */
.footer{position:absolute;top:2560px;left:0;width:1200px;height:290px;background:var(--dark);color:#ddd;display:flex;padding:34px 72px 0;gap:50px}
.footer h6{font-size:20px;font-weight:500;color:var(--white);text-transform:uppercase;margin-bottom:14px}
.map{width:240px;height:160px;background:linear-gradient(135deg,#e4e2dc,#cfd8c8)}
.office{width:220px}
.office li{list-style:none;display:flex;gap:10px;align-items:flex-start;font-size:14px;line-height:1.35;margin-bottom:12px}
.office li i{flex:none;width:22px;height:22px;background:var(--blue);display:flex;align-items:center;justify-content:center}
.office svg{width:12px;height:12px}
.footer-brand{margin-left:auto;text-align:center;padding-top:40px}
.footer-brand .brand{color:var(--white);font-size:64px}
.social{display:flex;gap:14px;justify-content:center;margin-top:16px}
.social span{width:38px;height:38px;background:#4a4a4d}
.bottom-bar{position:absolute;top:2850px;left:0;width:1200px;height:54px;background:var(--darker);color:#bbb;font-size:14px;text-align:center;line-height:54px}
.bottom-bar b{color:var(--blue-light);font-weight:500}
</style>
</head>
<body>

<header class="site-nav">
  <div class="brand">MOLAW</div>
  <ul class="menu">
    <li class="active">HOME</li>
    <li>ABOUT US</li>
    <li>PRACTICE AREAS</li>
    <li>BLOG</li>
    <li>CONTACT US</li>
  </ul>
</header>

<section class="hero" role="img" aria-label="Photo of a snow-capped California mountain under a pale blue sky">
  <div class="hero-text">
    <h1>MARWICK &amp; OSTRAND</h1>
    <p>STRONG REPUTATIONS DON'T<br>GO UNNOTICED</p>
  </div>
</section>

<section class="welcome">
  <h2 class="section-title">Welcome to <span>MOLAW</span></h2>
  <p>After practicing in both the private and public sector for several years, Elena Marwick and Dev Ostrand joined their legal expertise and formed Marwick &amp; Ostrand Law in 2015. With a combined 15 years of experience, Elena and Dev specialize in Civil Litigation, Family Law, Immigration and Criminal Defense. Their goal is to provide their clients with the best possible outcome in each and every case.</p>
  <span class="btn">Read More</span>
</section>

<section class="practice">
  <h2 class="section-title">Area's of Practice</h2>
  <div class="practice-grid">
    <div class="practice-card">
      <svg viewBox="0 0 130 130" fill="none" stroke="#fff" stroke-width="2">
        <circle cx="65" cy="65" r="62"/>
        <path d="M65 34v56M50 92h30M38 44h54M38 44l-12 26h24zM92 44l-12 26h24zM26 70a12 6 0 0 0 24 0M80 70a12 6 0 0 0 24 0"/>
      </svg>
      <h3>Business Law</h3>
    </div>
    <div class="practice-card">
      <svg viewBox="0 0 130 130" fill="none" stroke="#fff" stroke-width="2">
        <circle cx="65" cy="65" r="62"/>
        <circle cx="45" cy="40" r="8"/><circle cx="85" cy="40" r="8"/><circle cx="65" cy="62" r="6"/>
        <path d="M36 96V54h18v42M76 96V54h18v42M59 96V74h12v22"/>
      </svg>
      <h3>Family Law</h3>
    </div>
    <div class="practice-card">
      <svg viewBox="0 0 130 130" fill="none" stroke="#fff" stroke-width="2">
        <circle cx="65" cy="65" r="62"/>
        <circle cx="47" cy="72" r="16"/><circle cx="83" cy="72" r="16"/>
        <path d="M47 56v-8M83 56v-8M47 48c6-10 30-10 36 0"/>
      </svg>
      <h3>Criminal Defense</h3>
    </div>
  </div>
</section>

<section class="contact">
  <h2 class="section-title">Contact Us</h2>
  <div class="contact-form">
    <div class="field">Name</div>
    <div class="field">Email</div>
    <div class="field wide">Message</div>
    <span class="btn">Submit</span>
  </div>
</section>

<section class="team">
  <h2 class="section-title">Our Team</h2>
  <div class="team-grid">
    <div class="member">
      <div class="photo" role="img" aria-label="Portrait photo of attorney Elena R. Marwick"></div>
      <div>
        <h4>Elena R. Marwick</h4>
        <p>Elena Marwick founder and partner, is a California native who grew up in the same community she serves.</p>
        <span class="more">Read More</span>
      </div>
    </div>
    <div class="member">
      <div class="photo" role="img" aria-label="Portrait photo of attorney Dev S. Ostrand"></div>
      <div>
        <h4>Dev S. Ostrand</h4>
        <p>Dev Ostrand is a founding partner of Marwick &amp; Ostrand Law. After years of helping clients at other firms and litigation, he chose...</p>
        <span class="more">Read More</span>
      </div>
    </div>
  </div>
</section>

<section class="blog">
  <h2 class="section-title">Latest Blog</h2>
  <div class="blog-grid">
    <article class="post">
      <div class="thumb" role="img" aria-label="Photo of hands in handcuffs" style="background:linear-gradient(135deg,#8ea4bb,#c9b7a4)">
        <div class="date"><b>05</b><span>Apr</span></div>
      </div>
      <h5>Lorem ipsum is simply dummy text of the printing</h5>
      <p>Lorem ipsum is simply dummy text of the printing and typesetting industry. Lorem ipsum has been the industry standard...</p>
      <span class="more">Read More</span>
    </article>
    <article class="post">
      <div class="thumb" role="img" aria-label="Photo of a California city skyline at dusk" style="background:linear-gradient(180deg,#3b5d8a,#7fa2c6 60%,#2c3e55)">
        <div class="date"><b>05</b><span>Apr</span></div>
      </div>
      <h5>Lorem ipsum is simply dummy text of the printing</h5>
      <p>Lorem ipsum is simply dummy text of the printing and typesetting industry. Lorem ipsum has been the industry standard...</p>
      <span class="more">Read More</span>
    </article>
    <article class="post">
      <div class="thumb" role="img" aria-label="Photo of a couple reviewing documents at home" style="background:linear-gradient(135deg,#d9d4cc,#a9a39a)">
        <div class="date"><b>05</b><span>Apr</span></div>
      </div>
      <h5>Lorem ipsum is simply dummy text of the printing</h5>
      <p>Lorem ipsum is simply dummy text of the printing and typesetting industry. Lorem ipsum has been the industry standard...</p>
      <span class="more">Read More</span>
    </article>
  </div>
</section>

<footer class="footer">
  <div>
    <h6>Get Directions</h6>
    <div class="map" role="img" aria-label="Street map showing the office location"></div>
  </div>
  <div class="office">
    <h6>Office Address 1</h6>
    <ul>
      <li><i><svg viewBox="0 0 12 12"><path d="M6 0a4 4 0 0 0-4 4c0 3 4 8 4 8s4-5 4-8a4 4 0 0 0-4-4z" fill="#fff"/></svg></i>Valley Office</li>
      <li><i><svg viewBox="0 0 12 12"><path d="M6 0a4 4 0 0 0-4 4c0 3 4 8 4 8s4-5 4-8a4 4 0 0 0-4-4z" fill="#fff"/></svg></i>1450 Harbor St, Suite 210<br>Alder Creek, CA 90001</li>
      <li><i><svg viewBox="0 0 12 12"><path d="M2 1l3 0 1 3-2 1a7 7 0 0 0 3 3l1-2 3 1v3c-6 0-9-3-9-9z" fill="#fff"/></svg></i>(555) 555-0142</li>
      <li><i><svg viewBox="0 0 12 12"><path d="M2 1l3 0 1 3-2 1a7 7 0 0 0 3 3l1-2 3 1v3c-6 0-9-3-9-9z" fill="#fff"/></svg></i>(555) 555-0178</li>
    </ul>
  </div>
  <div class="office">
    <h6>Office Address 2</h6>
    <ul>
      <li><i><svg viewBox="0 0 12 12"><path d="M6 0a4 4 0 0 0-4 4c0 3 4 8 4 8s4-5 4-8a4 4 0 0 0-4-4z" fill="#fff"/></svg></i>Coastal Office</li>
      <li><i><svg viewBox="0 0 12 12"><path d="M6 0a4 4 0 0 0-4 4c0 3 4 8 4 8s4-5 4-8a4 4 0 0 0-4-4z" fill="#fff"/></svg></i>780 Ridgeview Blvd<br>Harbor Point, CA 90002</li>
      <li><i><svg viewBox="0 0 12 12"><path d="M2 1l3 0 1 3-2 1a7 7 0 0 0 3 3l1-2 3 1v3c-6 0-9-3-9-9z" fill="#fff"/></svg></i>(555) 555-0163</li>
      <li><i><svg viewBox="0 0 12 12"><path d="M1 2h10v8H1zM1 2l5 4 5-4" fill="none" stroke="#fff"/></svg></i>info@molaw-example.com</li>
    </ul>
  </div>
  <div class="footer-brand">
    <div class="brand">MOLAW</div>
    <div class="social"><span></span><span></span><span></span></div>
  </div>
</footer>

<div class="bottom-bar">© <b>MOLAW</b> - 2017. All Rights Reserved</div>

</body>
</html>
```